Hollow Breeze - New Product needs a Label

We need a package label for a new project that will come to market soon. The company is based in Canada and will need to show 'Made in Canada' with a Canadian flag.

The product is called Hollow Breeze. It is an odour eliminator. It will be in a dark brown plastic container that can be opened and left open in a room.

It can be used to help eliminate a number of different types of smoke; cigarette, pot or even fireplace smoke. We believe that 'no one should know what you smoke'.

We would like to see designs that reflect the intent of the product - to cover smoke. So far we've only thought that smokey colours like smokey green, smokey lavender and smokey grey or other grey tone colours would make sense. Update: I have removed the image that I 'doodled' on my own because I think it's been taken too literally. Please give me a fresh look at what an odor eliminator image could be.

Label dimensions are 11.25"x2.25"
Key wording:

Product Name: Hollow Breeze
Tag line: No one needs to know what you smoke
Also needs to include:
Directions
Remove the lid and place the container in any room where smoke is present. The contents will evaporate, neutralizing odours.

Net Wt. 14 0z. - 400 G
A spot for adding a bar code for scanners

Target Market(s)

Cigarette smokers / pot smokers / people with fire places or people who share a home with any of those categories

Requirements
Must have
• a label that fits the dimensions 11.25"x2.25" and the text / components outlined in the description
Nice to have
• A bit of humour, a sense of natural products

```html
<!DOCTYPE html>
<html lang="en">
<head>
<meta charset="utf-8">
<title>Hollow Breeze – Odour Eliminator Label</title>
<link href="https://fonts.googleapis.com/css2?family=Montserrat:wght@300;400;500;600;700;800&family=Archivo:wght@400;700;900&display=swap" rel="stylesheet">
<style>
  :root {
    --page: #f2f2f4;
    --label-black: #050707;
    --smoke-deep: #0b3a2f;
    --smoke-green: #1f7a5e;
    --smoke-mist: #2f9a78;
    --white: #ffffff;
    --ink: #111111;
    --badge-red: #d7192a;
  }
  * { margin: 0; padding: 0; box-sizing: border-box; }
  html, body {
    width: 1200px; height: 1058px; overflow: hidden;
    background: var(--page);
    font-family: "Montserrat", sans-serif;
  }
  .label {
    position: absolute; left: 20px; top: 413px;
    width: 1160px; height: 232px;
    background: var(--label-black);
    overflow: hidden;
    box-shadow: 0 2px 6px rgba(0,0,0,.25);
  }
  .label__smoke {
    position: absolute; inset: 0;
    background:
      radial-gradient(ellipse 260px 120px at 560px 140px, rgba(31,122,94,.55), transparent 70%),
      radial-gradient(ellipse 300px 140px at 900px 90px, rgba(47,154,120,.5), transparent 70%),
      radial-gradient(ellipse 240px 130px at 1080px 200px, rgba(31,122,94,.45), transparent 70%),
      radial-gradient(ellipse 200px 110px at 420px 40px, rgba(11,58,47,.6), transparent 70%),
      linear-gradient(90deg, var(--label-black) 28%, rgba(11,58,47,.6) 60%, rgba(11,58,47,.8) 100%);
  }
  .directions {
    position: absolute; left: 68px; top: 50px; width: 250px;
    color: var(--white); font-size: 11.6px; line-height: 14px;
    text-align: center;
  }
  .barcode-spot {
    position: absolute; left: 83px; top: 145px;
    width: 126px; height: 56px; background: var(--white);
  }
  .origin-badge {
    position: absolute; left: 225px; top: 130px;
    width: 80px; height: 80px; border-radius: 50%;
    background: var(--white); border: 10px solid var(--badge-red);
  }
  .brand {
    position: absolute; left: 427px; top: 30px; width: 300px;
    text-align: center; color: var(--white);
  }
  .brand__name {
    font-weight: 700; font-size: 56px; line-height: 52px;
    letter-spacing: 1px;
  }
  .brand__rule {
    width: 222px; height: 1.5px; background: var(--white);
    margin: 6px auto 0;
  }
  .brand__type {
    font-weight: 400; font-size: 16px; letter-spacing: .5px;
    margin-top: 1px;
  }
  .tagline {
    position: absolute; left: 501px; top: 178px;
    width: 302px; height: 17px; border-radius: 9px;
    background: var(--white); color: var(--ink);
    font-size: 10.5px; font-weight: 500; text-align: center; line-height: 17px;
  }
  .net-weight {
    position: absolute; left: 501px; top: 199px; width: 302px;
    text-align: center; color: var(--white);
    font-size: 9.5px; font-weight: 600;
  }
  .nutrition {
    position: absolute; left: 837px; top: 34px;
    width: 277px; height: 163px;
    border: 1px solid var(--white); color: var(--white);
    padding: 3px 3px; font-family: "Archivo", sans-serif;
  }
  .nutrition__title { font-weight: 900; font-size: 22px; line-height: 23px; border-bottom: 1px solid var(--white); }
  .nutrition__row { display: flex; justify-content: space-between; font-size: 6px; line-height: 8px; }
  .nutrition__row--bold { font-weight: 700; }
  .nutrition__row--indent { padding-left: 8px; }
  .nutrition__row--indent2 { padding-left: 16px; }
  .nutrition__bar { height: 4px; background: var(--white); margin: 1px 0; }
  .nutrition__cal { display: flex; justify-content: space-between; font-weight: 700; font-size: 12px; line-height: 14px; }
  .nutrition__cal span:last-child { font-size: 15px; }
  .nutrition__line { border-top: .6px solid var(--white); }
</style>
</head>
<body>
  <div class="label">
    <div class="label__smoke" role="img" aria-label="Dark green smoke wisps drifting across a black background"></div>

    <p class="directions">Directions<br>Remove the lid and place the container in any room where smoke is present. The contents will evaporate, neutralizing odours.</p>
    <div class="barcode-spot"></div>
    <div class="origin-badge"></div>

    <div class="brand">
      <div class="brand__name">HOLLOW<br>BREEZE</div>
      <div class="brand__rule"></div>
      <div class="brand__type">ODOUR ELIMINATOR</div>
    </div>
    <div class="tagline">NO ONE NEEDS TO KNOW WHAT YOU SMOKE</div>
    <div class="net-weight">Net Wt. 14 0z. - 400 G</div>

    <div class="nutrition">
      <div class="nutrition__title">Nutrition Facts</div>
      <div class="nutrition__row"><span>4 servings per container/6 raciones por envase</span></div>
      <div class="nutrition__row nutrition__row--bold"><span>Serving size</span><span>1 cup/1 taza (180g)</span></div>
      <div class="nutrition__bar"></div>
      <div class="nutrition__row nutrition__row--bold"><span>Amount per serving/Cantidad por porción</span></div>
      <div class="nutrition__cal"><span>Calories/Calorías</span><span>245</span></div>
      <div class="nutrition__line"></div>
      <div class="nutrition__row nutrition__row--bold"><span></span><span>% Daily Value*/% Valor diario*</span></div>
      <div class="nutrition__row"><span><b>Total Fat/Grasa total</b> 12g</span><span>14%</span></div>
      <div class="nutrition__row nutrition__row--indent"><span>Saturated Fat/Grasa Saturada 2g</span><span>10%</span></div>
      <div class="nutrition__row nutrition__row--indent"><span>Trans Fat/Grasa Trans 0g</span><span></span></div>
      <div class="nutrition__row"><span><b>Cholesterol/Colesterol</b> 8mg</span><span>3%</span></div>
      <div class="nutrition__row"><span><b>Sodium/Sodio</b> 210mg</span><span>9%</span></div>
      <div class="nutrition__row"><span><b>Total Carbohydrate/Carbohidrato Total</b> 34g</span><span>12%</span></div>
      <div class="nutrition__row nutrition__row--indent"><span>Dietary Fiber/Fibra Dietética 7g</span><span>25%</span></div>
      <div class="nutrition__row nutrition__row--indent"><span>Total Sugars/Azúcares Totales 5g</span><span></span></div>
      <div class="nutrition__row nutrition__row--indent2"><span>Includes 4g Added Sugars/Incluye 4 g de azúcares añadidos</span><span>8%</span></div>
    </div>
  </div>
</body>
</html>
```